Poem Handwritten by Veteran while in the jungle of Vietnam

My parents are celebrating their 50th wedding anniversary this year. I wanted to give them a very memorable gift. On my parents 2nd anniversary, my father was stationed in Vietnam. On that night he was in the jungle waiting till morning and wrote a poem to my mother using his pant leg as paper. I would like this poem to typographically designed to be framed and hung on the wall.

I have attached a picture of the poem below. It will need to be 11x14 when printed for framing. It would be great if there was background or artwork to make it more visually interesting, perhaps in a watercolor. My parents have a transitional style. I have attached some possible color schemes as well. Cool greens, blue, neutral grays, with hints of berries or highlights of yellow. These are just a guide, I would be open to your interpretations.

Thank you for your help. This will hopefully be a gift they will truly treasure as much as the poem itself.

Target Market(s)

My parents who are excited to be celebrating their 50th wedding anniversary. It should have a transitional, mature style.

Font styles to use
Serif
Script

Requirements
Must have
• The poem, typographically designed. There can be a mix of fonts, but legibility is critically important.
• Now that some designs have come through I wanted to give some more guidance of what I'm looking for. I want something that feels sophisticated and artistic.
Nice to have
• A background or art work, using the color schemes attached as a guide. I am really liking the designs that have a full color landscape artwork in the background. The fonts should be elegant and formal. I really like the romantic, muted colors. I had trouble finding similar projects online in the style I wanted until I cam across wedding invites. Those seem to be the most applicable. I've added pictures of some so you can get a sense of what I'm looking for. I am really liking the jungle foliage, starry skies or sunrises.
Should not have
• Cartoon caricatures, fonts that are too illegible when printed. I'm not liking anything whimsical. I don't like the very bright colors for this project.

```html
<!DOCTYPE html>
<html lang="en">
<head>
<meta charset="utf-8">
<title>Walter's Anniversary Poem</title>
<link rel="stylesheet" href="https://fonts.googleapis.com/css2?family=Arimo&family=Kaushan+Script&display=swap">
<style>
  :root {
    --ink-bg: #2a2a2a;
    --frame: #e8dcd7;
    --verse: #ffffff;
    --title: #f1e6e2;
    --foliage: #8f8583;
  }
  * { margin: 0; padding: 0; box-sizing: border-box; }
  html, body { width: 943px; height: 1200px; overflow: hidden; background: var(--ink-bg); }
  .poster { position: relative; width: 943px; height: 1200px; background: var(--ink-bg); overflow: hidden; }
  .foliage { position: absolute; inset: 0; width: 943px; height: 1200px; }
  .frame {
    position: absolute; left: 88px; top: 131px; width: 762px; height: 939px;
    border: 2px solid var(--frame);
  }
  .poem-title, .poem-dateline {
    position: absolute; left: 0; width: 943px; text-align: center;
    font-family: "Kaushan Script", cursive; color: var(--title); line-height: 1.2;
  }
  .poem-title { top: 110px; font-size: 31px; }
  .poem-dateline { top: 1053px; font-size: 23px; }
  .poem-title span, .poem-dateline span { background: var(--ink-bg); padding: 0 8px; }
  .verse-column {
    position: absolute; font-family: "Arimo", Arial, sans-serif;
    font-size: 16.7px; line-height: 19.2px; color: var(--verse); white-space: nowrap;
  }
  .verse-column.left { left: 146px; top: 182px; }
  .verse-column.right { left: 509px; top: 482px; }
  .stanza { margin-bottom: 19.2px; }
</style>
</head>
<body>
<div class="poster">
  <svg class="foliage" viewBox="0 0 943 1200">
    <defs>
      <filter id="soft" x="-20%" y="-20%" width="140%" height="140%"><feGaussianBlur stdDeviation="28"/></filter>
    </defs>
    <g role="img" aria-label="Line-drawn jungle foliage and flowers climbing the right side" filter="url(#soft)" fill="var(--foliage)">
      <ellipse cx="830" cy="150" rx="130" ry="110" opacity="0.35"/>
      <ellipse cx="880" cy="420" rx="90" ry="200" opacity="0.3"/>
      <ellipse cx="860" cy="720" rx="100" ry="170" opacity="0.3"/>
      <ellipse cx="620" cy="1150" rx="160" ry="70" opacity="0.28"/>
    </g>
    <g role="img" aria-label="Line-drawn leaves, ferns and berries in the lower left corner" filter="url(#soft)" fill="var(--foliage)">
      <ellipse cx="90" cy="760" rx="110" ry="150" opacity="0.3"/>
      <ellipse cx="170" cy="1000" rx="190" ry="170" opacity="0.32"/>
      <ellipse cx="330" cy="1140" rx="140" ry="80" opacity="0.28"/>
    </g>
  </svg>

  <div class="frame"></div>
  <h1 class="poem-title"><span>Walter's Anniversary Poem</span></h1>

  <div class="verse-column left">
    <p class="stanza">Life’s journey began with a challenge,<br>It was heralded far and near,<br>The road led on forever,<br>It’s completion was known to be dear.</p>
    <p class="stanza">From the garden of light it proceeded,<br>To the valleyof shadows it led.<br>Thorns and thistles adorned it,<br>Past abyss and crevice it sped.</p>
    <p class="stanza">The brave surged forward with courage,<br>The wise undaunted pressed on.<br>The mighty held high their banner,<br>We all awaited the dawn.</p>
    <p class="stanza">Though the pitfalls and hazards were many,<br>The pathway was clearly in view.<br>Straight and sure it glided,<br>Its course we knew to be true.</p>
    <p class="stanza">I knew you, Sweetheart, beforehand,<br>So precious and sweet were you,<br>Our moments of bliss were priceless,<br>Each day brought us joy anew.</p>
  </div>

  <div class="verse-column right">
    <p class="stanza">The call to progression beckoned,<br>At last I would have my chance--<br>To clasp you to me forever,<br>And seal our divine romance.</p>
    <p class="stanza">I eagerly started the journey,<br>Though with sorrow, I left you behind.<br>With courage and faith I continued,<br>For I knew, that you later I’d find.</p>
    <p class="stanza">I diligently searched for you, Darling,<br>The road was both bleack and fair.<br>Though the years grew long in number,<br>I did not give up in dispair.</p>
    <p class="stanza">At last in the distance I saw you,<br>So beautiful, lovely, and sweet”<br>Your attention I struggled to capture,<br>Your love I wrested to meet.</p>
    <p class="stanza">What rapture was mine in fulfillment,<br>As now together we stand.<br>To cherish and love each other,<br>While our plans and dreams expand.</p>
    <p class="stanza">I love you, Darling, forever,<br>My life you have made replete.<br>Our eternal mansion beckons,<br>Your love has made it complete.</p>
  </div>

  <p class="poem-dateline"><span>20 July 1970. Monday. LZ Meridian</span></p>
</div>
</body>
</html>
```